Harborlight Capital Estates business card

We are a real estate advisory and investment company. We are specialized in assisting high networth individuals to invest in real estate overseas. We deliver a very personalized service, anticipating all the potential challenges an investor can face, and making it easy and safe for them. We also co-invest with our clients, assuring them that each project will be looked after as it is our own, and at the same time giving them the extra booth on confidence to invest.

We need a business card design. The business card must have a very premium, high-end look, reflecting principles like "commitment", "trust" and "timeless (but contemporary)". We look for long term relationships with our clients, and we grow with their referrals. We are all about conquering the confidence of the clients by always delivering above the expectations performance.

Target Market(s)

High net worth individuals.

Industry/Entity Type

Real Estate

Contact Information for Business Card

Please consider places on the business card for:

Name
Function (bellow name in smaller size text)

Mobile phone
E-mail
Skype ID
WeChat ID

Adress (3 lines)

Also include the following locations references:
PORTUGAL * DUBAI * HONG KONG

Website: www.hcestates-example.com

Requirements
Must have
• Company Logo

```html
<!DOCTYPE html>
<html lang="en">
<head>
<meta charset="utf-8">
<title>Harborlight Capital Estates – Business Card</title>
<link rel="stylesheet" href="https://fonts.googleapis.com/css2?family=Cinzel:wght@500&family=Montserrat:wght@400;600&display=swap">
<style>
  :root {
    --backdrop: #2b2b2d;
    --ink: #0b0b0b;
    --paper: #ffffff;
    --accent: #29abe2;
    --silver: #9a9a9a;
    --marker: #8c8c8c;
    --text-light: #f2f2f2;
  }
  * { margin: 0; padding: 0; box-sizing: border-box; }
  html, body { width: 1200px; height: 900px; overflow: hidden; }
  body { background: var(--backdrop); font-family: "Montserrat", sans-serif; position: relative; }

  .card {
    position: absolute;
    width: 520px;
    height: 300px;
    border-radius: 18px;
    overflow: hidden;
  }

  /* Front */
  .card-front { left: 100px; top: 110px; background: var(--ink); }
  .front-brand {
    position: absolute; left: 0; right: 0; top: 106px;
    text-align: center; white-space: nowrap;
    font-weight: 600; font-size: 24px; line-height: 30px; letter-spacing: 1px;
    color: var(--accent);
  }
  .front-rule {
    position: absolute; left: 80px; right: 80px; top: 146px;
    height: 1px; background: var(--silver);
  }
  .front-web {
    position: absolute; left: 0; right: 0; top: 164px;
    text-align: center; font-size: 15px; color: var(--text-light);
  }
  .front-web .domain { color: var(--accent); }
  .front-locations {
    position: absolute; left: 0; right: 0; top: 198px;
    text-align: center; font-weight: 600; font-size: 15px;
    letter-spacing: 1px; color: var(--text-light);
  }
  .front-locations .sep { color: var(--accent); margin: 0 6px; }

  /* Back */
  .card-back { left: 580px; top: 480px; background: var(--paper); }
  .back-shape { position: absolute; inset: 0; }
  .name-marker {
    position: absolute; right: 0; top: 24px; width: 16px; height: 26px;
    background: var(--marker);
  }
  .back-name { position: absolute; right: 28px; top: 24px; text-align: right; }
  .back-name .person {
    font-family: "Cinzel", serif; font-weight: 500; font-size: 19px;
    color: var(--accent); letter-spacing: 0.5px;
  }
  .back-name .role { font-size: 12px; color: var(--silver); margin-top: 2px; }
  .back-brand {
    position: absolute; left: 30px; top: 96px;
    font-weight: 600; font-size: 17px; letter-spacing: 0.5px;
    color: var(--accent); line-height: 1.25;
  }
  .back-contacts {
    position: absolute; right: 22px; top: 150px;
    list-style: none; text-align: right;
    font-size: 13px; color: var(--text-light); line-height: 20px;
  }
  .back-contacts li { display: flex; justify-content: flex-end; align-items: center; gap: 8px; }
  .back-contacts svg { width: 11px; height: 11px; }
  .back-address {
    position: absolute; left: 225px; bottom: 18px;
    font-size: 14px; color: var(--text-light); line-height: 18px;
    font-style: normal;
  }
</style>
</head>
<body>

<section class="card card-front">
  <div class="front-brand">HARBORLIGHT CAPITAL ESTATES</div>
  <div class="front-rule"></div>
  <div class="front-web">www.<span class="domain">hcestates-example</span>.com</div>
  <div class="front-locations">PORTUGAL<span class="sep">-</span>DUBAI<span class="sep">-</span>HONG KONG</div>
</section>

<section class="card card-back">
  <svg class="back-shape" viewBox="0 0 520 300" preserveAspectRatio="none" aria-hidden="true">
    <path d="M40,300 Q300,60 520,70 L520,300 Z" fill="#0b0b0b"/>
    <path d="M40,300 Q300,60 520,70" fill="none" stroke="#29abe2" stroke-width="5"/>
  </svg>
  <div class="name-marker"></div>
  <div class="back-name">
    <div class="person">MARCUS ELLWOOD</div>
    <div class="role">Function</div>
  </div>
  <div class="back-brand">HARBORLIGHT<br>CAPITAL ESTATES</div>
  <ul class="back-contacts">
    <li>+351 555-0148
      <svg viewBox="0 0 12 12"><path d="M2 1h3l1 3-1.5 1a7 7 0 0 0 2.5 2.5L8 6l3 1v3c0 .6-.4 1-1 1A9 9 0 0 1 1 2c0-.6.4-1 1-1z" fill="#29abe2"/></svg></li>
    <li>info@hcestates-example.com
      <svg viewBox="0 0 12 12"><rect x="1" y="2.5" width="10" height="7" fill="none" stroke="#29abe2" stroke-width="1.2"/><path d="M1 3l5 4 5-4" fill="none" stroke="#29abe2" stroke-width="1.2"/></svg></li>
    <li>www.hcestates-example.com
      <svg viewBox="0 0 12 12"><circle cx="6" cy="6" r="5" fill="none" stroke="#29abe2" stroke-width="1.2"/><path d="M1 6h10M6 1c-2.5 3-2.5 7 0 10M6 1c2.5 3 2.5 7 0 10" fill="none" stroke="#29abe2" stroke-width="1"/></svg></li>
  </ul>
  <address class="back-address">PO Box 4870<br>Harbor Plaza<br>QLD 4010</address>
</section>

</body>
</html>
```